Business card design for Luxury Real Estate

Using the corporate logo you have designed, please design a business card for a luxury real estate company in Thailand.

The brand is about elegance, calm, sophistication and luxury. The card should look clean, modern and be standard business card size. The background should be white to enable future scanning of the card (funky backgrounds result in poor card scanning results).

Text on Business Card (Front side) shall include the following:
- Corporate Logo
- Include the following business services underneath " Sales. Rentals. Investments. Financing."
- Name: Marisa Tevel
- Title: CEO, Founder
- mobile phone: +65 84219637 (Singapore), +66 7000 48261 (Thailand)
- email: marisa@goldenreedhaven.com
- skype: goldenreedhaven
- url: www.goldenreedhaven.com

Backside
- include same info but shall have Chinese name and title.

please use the attached additional language in mandarin for "sales. rentals. investments. financing."

Normal 0 false false false EN-US JA X-NONE 售和房租。投和融    

Target Market(s)

high net worth individuals, business men/ women, finance managers.

Industry/Entity Type

Real Estate

Requirements
Must have
• elegant, sophisticated, clean, modern look. appealing but comforting to the eye. should not be crowded and overcomplicated.

```html
<!DOCTYPE html>
<html lang="en">
<head>
<meta charset="utf-8">
<title>Golden Reed Haven — Business Card</title>
<link rel="stylesheet" href="https://fonts.googleapis.com/css2?family=Source+Sans+3:wght@400;600&display=swap">
<style>
  :root {
    --page-bg: #f2f2f0;
    --card-bg: #ffffff;
    --card-edge: #dcdcdc;
    --ink-dark: #2b2b2b;
    --ink-mid: #4a4a4a;
    --ink-soft: #6b6b6b;
    --gold: #c9a24a;
  }
  html, body {
    margin: 0;
    width: 1200px;
    height: 986px;
    overflow: hidden;
    background: var(--page-bg);
    font-family: "Source Sans 3", "Helvetica Neue", Arial, sans-serif;
  }
  .card {
    position: absolute;
    left: 100px;
    top: 184px;
    width: 1000px;
    height: 618px;
    background: var(--card-bg);
    border: 1px solid var(--card-edge);
    box-shadow: 0 6px 24px rgba(0,0,0,0.08);
  }
  .person {
    position: absolute;
    left: 552px;
    top: 60px;
  }
  .person__name {
    margin: 0;
    font-size: 34px;
    font-weight: 600;
    color: var(--ink-dark);
    line-height: 1;
  }
  .person__title {
    margin: 10px 0 0;
    font-size: 22px;
    font-weight: 400;
    color: var(--ink-mid);
  }
  .contacts {
    position: absolute;
    left: 552px;
    top: 180px;
    margin: 0;
    padding: 0;
    list-style: none;
    font-size: 19px;
    color: var(--ink-mid);
  }
  .contacts__row {
    display: flex;
    align-items: center;
    height: 30px;
  }
  .contacts__row--gap { margin-top: 7px; }
  .contacts__label {
    width: 16px;
    font-size: 12px;
    color: var(--ink-soft);
    text-transform: uppercase;
  }
  .contacts__dot {
    width: 5px;
    height: 5px;
    border-radius: 50%;
    background: var(--gold);
    margin: 0 9px 0 4px;
  }
  .brand {
    position: absolute;
    left: 81px;
    top: 432px;
    font-size: 50px;
    font-weight: 400;
    color: var(--ink-mid);
    letter-spacing: -0.5px;
    line-height: 1;
  }
  .services {
    position: absolute;
    left: 81px;
    top: 548px;
    display: flex;
    align-items: center;
    font-size: 16px;
    letter-spacing: 3px;
    color: var(--ink-mid);
    text-transform: uppercase;
  }
  .services__dot {
    width: 5px;
    height: 5px;
    background: var(--gold);
    border-radius: 50%;
    margin: 0 12px 0 9px;
  }
</style>
</head>
<body>
  <article class="card">
    <header class="person">
      <h1 class="person__name">Marisa Tevel</h1>
      <p class="person__title">CEO, Founder</p>
    </header>

    <ul class="contacts">
      <li class="contacts__row"><span class="contacts__label">T</span><span class="contacts__dot"></span>+65 84219637 (Singapore)</li>
      <li class="contacts__row"><span class="contacts__label"></span><span class="contacts__dot"></span>+66 7000 48261 (Thailand)</li>
      <li class="contacts__row contacts__row--gap"><span class="contacts__label">E</span><span class="contacts__dot"></span>marisa@goldenreedhaven.com</li>
      <li class="contacts__row contacts__row--gap"><span class="contacts__label">S</span><span class="contacts__dot"></span>goldenreedhaven</li>
      <li class="contacts__row contacts__row--gap"><span class="contacts__label">W</span><span class="contacts__dot"></span>www.goldenreedhaven.com</li>
    </ul>

    <div class="brand">Golden Reed Haven</div>

    <div class="services">
      Sales<span class="services__dot"></span>Rentals<span class="services__dot"></span>Investments<span class="services__dot"></span>Financing
    </div>
  </article>
</body>
</html>
```